Talvin Crestline Homes needs a business card

We need a business card for a new company in Canada, Ontario. Our company is all about luxury contraction homes for our clients. Our product and services are custom projects design. Under the business logo that will be created, we want a slogan that will be a memorable phrase for consumers to remember us to tell their friends and relatives.

Additional infomation
- Brennick Solvadeu
- President / Ceo
-415.390.7628

Find point what luxury construction products and services can be done

We like to see colors:
- #663300
- and something other colors or color that would attract the client needs and wants

The final design should communicate leads from new or old clients that will grow our empire. Most of all, we try to work among the budget that clients want

NOTE
- we also need an icon for the business (Example: Pictoloop, Friendvane, and Chattorq icons)
- We want the company name to be remembered easily for clients and our distributors who would get our orders.
- we need an icon on the business cards: Friendvane and Pictoloop.

Thanks,
Talvin Crestline Homes

```html
<!DOCTYPE html>
<html lang="en">
<head>
<meta charset="utf-8">
<title>Talvin Crestline Homes — Business Card</title>
<link href="https://fonts.googleapis.com/css2?family=Arimo:wght@400;700&family=Oswald:wght@500&display=swap" rel="stylesheet">
<style>
  :root {
    --brown: #663300;
    --brown-deep: #4a2500;
    --wood-dark-a: #7a4514;
    --wood-dark-b: #5e3008;
    --wood-light-a: #ecd3a8;
    --wood-light-b: #d4b384;
    --ink-light: #ffffff;
    --ink-plate: #6b3a0c;
    --page: #eef0f1;
  }
  * { box-sizing: border-box; margin: 0; padding: 0; }
  html, body { width: 1200px; height: 900px; overflow: hidden; background: var(--page); }
  body { font-family: "Arimo", Arial, sans-serif; color: var(--ink-light); }

  .sheet { position: relative; width: 1200px; height: 900px; }
  .card {
    position: absolute; left: 240px; width: 720px; height: 411px;
    border-radius: 4px; overflow: hidden;
    box-shadow: 0 6px 18px rgba(0,0,0,.18);
  }
  .card--front { top: 28px; }
  .card--back { top: 461px; background: var(--brown); }

  .wood-dark {
    position: absolute; inset: 0;
    background: linear-gradient(100deg, var(--wood-dark-a) 0%, var(--wood-dark-b) 55%, #6c3a0e 100%);
  }
  .wood-light {
    background: linear-gradient(95deg, var(--wood-light-a), var(--wood-light-b) 60%, #e6c99a);
  }

  .brand { position: absolute; text-align: center; }
  .brand__name { font-weight: 700; font-size: 40px; letter-spacing: -0.5px; line-height: 1; }
  .brand__tagline { font-size: 12.5px; letter-spacing: .4px; margin-top: 6px; }
  .card--front .brand { left: 0; right: 0; top: 172px; }
  .card--back .brand { left: 56px; top: 150px; text-align: left; }
  .card--back .brand__name { font-size: 34px; }
  .card--back .brand__tagline { font-size: 11px; }

  .edge-strip { position: absolute; left: 0; top: 0; width: 16px; height: 100%; }
  .edge-tab { position: absolute; left: 0; top: 255px; width: 58px; height: 58px; border-radius: 0 10px 10px 0; box-shadow: 3px 4px 0 var(--brown-deep); }

  .plate-band { position: absolute; right: 0; top: 28px; width: 330px; height: 92px; border-radius: 12px 0 0 12px; box-shadow: -6px 8px 0 var(--brown-deep); }
  .plate { position: absolute; right: 24px; top: 44px; width: 270px; color: var(--ink-plate); }
  .plate__name { font-family: "Oswald", "Arial Narrow", sans-serif; font-weight: 500; font-size: 30px; letter-spacing: .5px; line-height: 1.05; }
  .plate__role { font-size: 12px; font-weight: 700; letter-spacing: .8px; margin-top: 3px; padding-left: 40px; }

  .contact { position: absolute; list-style: none; font-size: 13.5px; }
  .contact li { display: flex; align-items: center; gap: 8px; height: 22px; }
  .contact svg { width: 15px; height: 15px; flex: none; }
  .contact--social { left: 430px; top: 150px; }
  .contact--social .mark { width: 11px; height: 11px; background: var(--ink-light); border-radius: 2px; flex: none; }
  .contact--social .network { font-weight: 700; }
  .contact--direct { left: 56px; top: 300px; font-size: 14.5px; }
</style>
</head>
<body>
<main class="sheet">

  <section class="card card--front" aria-label="Card front">
    <div class="wood-dark" role="img" aria-label="Dark walnut wood-grain texture"></div>
    <div class="brand">
      <p class="brand__name">Talvin Crestline Homes</p>
      <p class="brand__tagline">- HOME RENOVATIONS - CUSTOM PROJECT DESIGN -</p>
    </div>
  </section>

  <section class="card card--back" aria-label="Card back">
    <div class="edge-strip wood-light" role="img" aria-label="Light pine wood trim"></div>
    <div class="edge-tab wood-light" role="img" aria-label="Light pine wood tab"></div>

    <div class="plate-band wood-light" role="img" aria-label="Light pine wood name plate"></div>
    <div class="plate">
      <p class="plate__name">BRENNICK SOLVADEU</p>
      <p class="plate__role">PRESIDENT / CEO</p>
    </div>

    <div class="brand">
      <p class="brand__name">Talvin Crestline Homes</p>
      <p class="brand__tagline">- HOME RENOVATIONS - CUSTOM PROJECT DESIGN -</p>
    </div>

    <ul class="contact contact--social">
      <li><span class="mark"></span><span class="network">Pictoloop</span> brennick_solv</li>
      <li><span class="mark"></span><span class="network">Friendvane</span> Brennick Solvadeu</li>
      <li><span class="mark"></span><span class="network">Chattorq</span> 415.390.7628</li>
    </ul>

    <ul class="contact contact--direct">
      <li>
        <svg viewBox="0 0 16 16" aria-hidden="true"><circle cx="8" cy="8" r="8" fill="#fff"/><path d="M4 5.5h8v5H4z M4 5.5l4 3 4-3" fill="none" stroke="#663300" stroke-width="1.2"/></svg>
        hello@talvincrestline.ca
      </li>
      <li>
        <svg viewBox="0 0 16 16" aria-hidden="true"><g fill="none" stroke="#fff" stroke-width="1.2"><circle cx="8" cy="8" r="7"/><ellipse cx="8" cy="8" rx="3" ry="7"/><path d="M1 8h14M2.2 4.5h11.6M2.2 11.5h11.6"/></g></svg>
        talvincrestline.ca
      </li>
      <li>
        <svg viewBox="0 0 16 16" aria-hidden="true"><circle cx="8" cy="8" r="7" fill="none" stroke="#fff" stroke-width="1.2"/><path d="M5.3 4.2l1.4-.2.8 2-1 .8c.5 1.1 1.3 1.9 2.4 2.4l.8-1 2 .8-.2 1.4c-3.5.3-6.5-2.7-6.2-6.2z" fill="#fff"/></svg>
        415 390 7628
      </li>
    </ul>
  </section>

</main>
</body>
</html>
```